Football and Sports Management Agency Stationary

We have a logo, fonts, website and colour palette.
We need the logo refined by a proper designer and then business stationary designed. You can see on the website how it needs adjusting by a designers eye.
The company is a high end sports management company aiming to attract and represent professional athletes. The name Velorin is to indicate a 'Constellation of Stars' ie our clients. The dots on the star should be slightly different sizes to reflect that some clients will be bigger than others.
Colours:
#e6e6e6
#edd2a4
#caaa72 (main gold and also used on site)
#3f3f42
#001d38
#edeced (on website)
#191c23 (on website)
Font:
QT (velorin)
QT Melbrook (sports management)
We would like:
- Letterhead (word and indesign and PDF print format). I have attached an example for one I like. It's quiet a clean design with the contact details and address taking up only a small amount of room.
- Business card (dark on the back with the logo, personal details on the front). Only needs name, title, email, website and phone number. No company address (in PDF and indesign format)
- Powerpoint slide theme
- Logo in vector format for light and dark versions and single colour versions. And optimised web version
- Simple brand guide PDF showing colour, font and logo (a one/two page PDF)
Any questions, please ask.
NEW INFO:
Contact Details
Maren Solwick
Director
Mobile: +44 7630 218 977
Phone: +44 0113 872 604
Email: maren@velorinathletic.example
Web: velorinathletic.example
Corran Lodge, 14 Mill Bank Road, Stockport, SK4 9TW
Company number 40718362
Target Market(s)
Professional athletes, professional sports teams.
Industry/Entity Type
Management
Requirements
Must have
- NEW
- The designs must look cool, classy and high quality. My suggestion for this is to keep the text small and precise with uncomplicated design.
Nice to have
- Application of brand displayed on stationary and additional pieces of stationary branded.
- Draw some inspiration from the website. eg the slant angles used separate the sections.
Should not have
- Don't create new logos etc.

```html
<!DOCTYPE html>
<html lang="en">
<head>
<meta charset="utf-8">
<title>Velorin Sports Management – Slide Theme</title>
<link href="https://fonts.googleapis.com/css2?family=Montserrat:wght@500;600;700&family=Open+Sans:wght@400;600&display=swap" rel="stylesheet">
<style>
  :root{
    --page:#e9e9e9;
    --navy:#001d38;
    --navy-deep:#001428;
    --navy-light:#0b2a4a;
    --gold:#caaa72;
    --gold-light:#edd2a4;
    --white:#ffffff;
    --ink:#191c23;
  }
  *{box-sizing:border-box;margin:0;padding:0}
  html,body{width:1200px;height:795px;overflow:hidden;background:var(--page)}
  .board{position:relative;width:1200px;height:795px;font-family:"Open Sans",sans-serif}
  .slide{position:absolute;width:547px;height:307px;display:block;box-shadow:0 1px 3px rgba(0,0,0,.18)}
  .slide--cover{left:34px;top:38px}
  .slide--welcome{left:620px;top:38px}
  .slide--feature{left:34px;top:413px}
  .slide--services{left:620px;top:413px}
  .slide-label{position:absolute;width:547px;text-align:center;font-family:"Open Sans",sans-serif;font-size:26px;color:var(--ink);letter-spacing:.5px;line-height:1}
  .slide-label--top{top:358px}
  .slide-label--bottom{top:737px}
  .slide-label--left{left:34px}
  .slide-label--right{left:620px}
  .brand-name{font-family:"Montserrat",sans-serif;font-weight:600}
  .headline{font-family:"Montserrat",sans-serif;font-weight:600}
  .body-copy{font-family:"Open Sans",sans-serif}
</style>
</head>
<body>
<div class="board">

  <!-- Cover -->
  <svg class="slide slide--cover" viewBox="0 0 684 384" xmlns="http://www.w3.org/2000/svg">
    <defs>
      <linearGradient id="pitchGrad" x1="0" y1="0" x2="0" y2="1">
        <stop offset="0" stop-color="#b9b9b2"/>
        <stop offset=".3" stop-color="#6ea452"/>
        <stop offset="1" stop-color="#3f8530"/>
      </linearGradient>
    </defs>
    <rect width="684" height="384" fill="url(#pitchGrad)" role="img" aria-label="Photo of young players training on an artificial football pitch"/>
    <polyline points="395,0 180,195 375,384" fill="none" stroke="var(--gold)" stroke-width="4"/>
    <polyline points="412,0 200,195 395,384" fill="none" stroke="var(--gold-light)" stroke-width="2"/>
    <polyline points="470,110 525,195 430,290" fill="none" stroke="var(--white)" stroke-width="1.5"/>
    <polygon points="366,44 514,192 366,340 218,192" fill="none" stroke="var(--navy)" stroke-width="7"/>
    <polygon points="366,56 502,192 366,328 230,192" fill="var(--white)" fill-opacity=".9"/>
    <text class="brand-name" x="366" y="201" text-anchor="middle" font-size="26" fill="var(--navy)">Velorin</text>
  </svg>
  <div class="slide-label slide-label--top slide-label--left">COVER PAGE</div>

  <!-- Welcome -->
  <svg class="slide slide--welcome" viewBox="0 0 684 384" xmlns="http://www.w3.org/2000/svg">
    <defs>
      <radialGradient id="navyGlow" cx=".5" cy=".5" r=".75">
        <stop offset="0" stop-color="var(--navy-light)"/>
        <stop offset="1" stop-color="var(--navy-deep)"/>
      </radialGradient>
      <linearGradient id="playGrad" x1="0" y1="0" x2="0" y2="1">
        <stop offset="0" stop-color="#9fb7a4"/><stop offset="1" stop-color="#5e9a45"/>
      </linearGradient>
      <linearGradient id="portraitGrad" x1="0" y1="0" x2="1" y2="1">
        <stop offset="0" stop-color="#6b4a38"/><stop offset="1" stop-color="#c9c3bd"/>
      </linearGradient>
      <linearGradient id="bootGrad" x1="0" y1="0" x2="1" y2="1">
        <stop offset="0" stop-color="#d8c23a"/><stop offset=".5" stop-color="#c33b2a"/><stop offset="1" stop-color="#5aa03d"/>
      </linearGradient>
    </defs>
    <rect width="684" height="384" fill="url(#navyGlow)"/>
    <polyline points="105,125 180,52 255,125" fill="none" stroke="var(--white)" stroke-width="2.5"/>
    <polyline points="100,227 175,297 245,227" fill="none" stroke="var(--white)" stroke-width="2.5"/>
    <polyline points="182,113 225,70 328,172 225,282 165,222" fill="none" stroke="var(--gold)" stroke-width="4"/>
    <polyline points="273,147 300,172 273,197" fill="none" stroke="var(--white)" stroke-width="2.5"/>
    <text class="headline" x="40" y="178" font-size="31" font-weight="700" fill="var(--gold)">WELCOME</text>
    <text class="body-copy" x="42" y="200" font-size="8.5" font-weight="600" letter-spacing="2.6" fill="var(--white)">SUBTITLE GOES HERE</text>

    <polygon points="547,14 655,132 547,250 439,132" fill="none" stroke="var(--gold)" stroke-width="3"/>
    <polygon points="547,24 645,132 547,240 449,132" fill="url(#playGrad)" role="img" aria-label="Photo of two young players contesting the ball"/>
    <polygon points="440,185 525,270 440,355 355,270" fill="none" stroke="var(--white)" stroke-width="1.5"/>
    <polygon points="440,193 517,270 440,347 363,270" fill="url(#portraitGrad)" role="img" aria-label="Photo of a young player holding a football"/>
    <polygon points="615,205 697,287 615,369 533,287" fill="none" stroke="var(--white)" stroke-width="2"/>
    <polygon points="615,217 685,287 615,357 545,287" fill="url(#bootGrad)" role="img" aria-label="Photo of a player's boots and striped socks striking a ball"/>

    <circle cx="203" cy="367" r="2.5" fill="none" stroke="var(--white)"/>
    <line x1="206" y1="367" x2="255" y2="367" stroke="var(--white)"/>
    <text class="body-copy" x="342" y="370" text-anchor="middle" font-size="7" letter-spacing="1.6" fill="var(--white)">www.velorinathletic.example</text>
    <line x1="429" y1="367" x2="478" y2="367" stroke="var(--white)"/>
    <circle cx="481" cy="367" r="2.5" fill="none" stroke="var(--white)"/>
  </svg>
  <div class="slide-label slide-label--top slide-label--right">PAGE - 01</div>

  <!-- Feature -->
  <svg class="slide slide--feature" viewBox="0 0 684 384" xmlns="http://www.w3.org/2000/svg">
    <defs>
      <radialGradient id="navyGlow2" cx=".5" cy=".5" r=".75">
        <stop offset="0" stop-color="var(--navy-light)"/>
        <stop offset="1" stop-color="var(--navy-deep)"/>
      </radialGradient>
      <linearGradient id="stadiumGrad" x1="0" y1="0" x2="0" y2="1">
        <stop offset="0" stop-color="#cfd8e2"/><stop offset=".45" stop-color="#8a7d72"/><stop offset="1" stop-color="#3f7d36"/>
      </linearGradient>
    </defs>
    <rect width="684" height="384" fill="url(#navyGlow2)"/>
    <g fill="none" stroke="var(--white)">
      <circle cx="190" cy="192" r="137" stroke-width="1.5"/>
      <circle cx="190" cy="192" r="127" stroke-width="3"/>
      <circle cx="190" cy="192" r="117" stroke-width="1.5"/>
    </g>
    <circle cx="198" cy="192" r="88" fill="url(#stadiumGrad)" role="img" aria-label="Photo of a supporter watching a match in a packed stadium"/>
    <polygon points="190,64 303,262 76,262" fill="none" stroke="var(--gold)" stroke-width="5"/>
    <text class="headline" x="368" y="119" font-size="25" fill="var(--gold)">LOREM IPSUM IS</text>
    <text class="headline" x="368" y="150" font-size="25" fill="var(--gold)">SIMPLY</text>
    <text class="body-copy" x="369" y="202" font-size="9.5" font-weight="600" fill="var(--white)">Write Your Title</text>
    <g class="body-copy" font-size="6.6" fill="var(--white)">
      <text x="369" y="220">Lorem Ipsum is simply dummy text of the printing and typesetting industry. Lorem</text>
      <text x="369" y="231">Ipsum has been the industry's standard dummy text ever since the 1500s, when an</text>
      <text x="369" y="242">unknown printer took a galley of type and scrambled it to make a type specimen</text>
      <text x="369" y="253">book. It has survived not only five centuries.</text>
    </g>
    <line x1="370" y1="287" x2="411" y2="287" stroke="var(--gold)" stroke-width="2.5"/>
    <circle cx="203" cy="367" r="2.5" fill="none" stroke="var(--white)"/>
    <line x1="206" y1="367" x2="255" y2="367" stroke="var(--white)"/>
    <text class="body-copy" x="342" y="370" text-anchor="middle" font-size="7" letter-spacing="1.6" fill="var(--white)">www.velorinathletic.example</text>
    <line x1="429" y1="367" x2="478" y2="367" stroke="var(--white)"/>
    <circle cx="481" cy="367" r="2.5" fill="none" stroke="var(--white)"/>
  </svg>
  <div class="slide-label slide-label--bottom slide-label--left">PAGE - 02</div>

  <!-- Services -->
  <svg class="slide slide--services" viewBox="0 0 684 384" xmlns="http://www.w3.org/2000/svg">
    <defs>
      <radialGradient id="navyGlow3" cx=".6" cy=".5" r=".75">
        <stop offset="0" stop-color="var(--navy-light)"/>
        <stop offset="1" stop-color="var(--navy-deep)"/>
      </radialGradient>
      <linearGradient id="ballGrad" x1="0" y1="0" x2="0" y2="1">
        <stop offset="0" stop-color="#7fbf4c"/><stop offset="1" stop-color="#3e8a2c"/>
      </linearGradient>
    </defs>
    <rect width="684" height="384" fill="url(#navyGlow3)"/>
    <polygon points="0,0 340,0 150,384 0,384" fill="url(#ballGrad)" role="img" aria-label="Photo of a player resting a boot on a football on grass"/>
    <polygon points="340,0 357,0 167,384 150,384" fill="var(--white)"/>
    <line x1="348" y1="0" x2="158" y2="384" stroke="var(--navy)" stroke-width="1" stroke-dasharray="5 3"/>
    <circle cx="239" cy="195" r="67" fill="var(--navy)" stroke="var(--white)" stroke-width="13"/>
    <text class="headline" x="239" y="193" text-anchor="middle" font-size="16" fill="var(--gold)">LOREM IS</text>
    <text class="headline" x="239" y="212" text-anchor="middle" font-size="16" fill="var(--gold)">IPSUM</text>

    <g class="service">
      <circle cx="377" cy="82" r="14" fill="var(--white)"/>
      <circle cx="377" cy="82" r="7" fill="none" stroke="var(--navy)" stroke-width="1.3"/>
      <circle cx="377" cy="82" r="2.2" fill="var(--navy)"/>
      <text class="headline" x="362" y="116" font-size="9.5" fill="var(--white)">Text In Here</text>
      <g class="body-copy" font-size="6.4" fill="var(--white)"><text x="362" y="130">Lorem Ipsum is simply dummy</text><text x="362" y="141">text of the printing and type</text><text x="362" y="152">setting industry. Lorem Ipsum</text><text x="362" y="163">has been the industry's.</text></g>
    </g>
    <g class="service">
      <circle cx="538" cy="82" r="14" fill="var(--white)"/>
      <rect x="529" y="76" width="18" height="12" fill="none" stroke="var(--navy)" stroke-width="1.3"/>
      <line x1="538" y1="76" x2="538" y2="88" stroke="var(--navy)" stroke-width="1.1"/>
      <circle cx="538" cy="82" r="2.5" fill="none" stroke="var(--navy)" stroke-width="1"/>
      <text class="headline" x="523" y="116" font-size="9.5" fill="var(--white)">Text In Here</text>
      <g class="body-copy" font-size="6.4" fill="var(--white)"><text x="523" y="130">Lorem Ipsum is simply dummy</text><text x="523" y="141">text of the printing and type</text><text x="523" y="152">setting industry. Lorem Ipsum</text><text x="523" y="163">has been the industry's.</text></g>
    </g>
    <g class="service">
      <circle cx="377" cy="221" r="14" fill="var(--white)"/>
      <rect x="368" y="215" width="18" height="12" fill="none" stroke="var(--navy)" stroke-width="1.3"/>
      <path d="M371 215v12M374 215v12M377 215v12M380 215v12M383 215v12" stroke="var(--navy)" stroke-width=".8"/>
      <text class="headline" x="362" y="255" font-size="9.5" fill="var(--white)">Text In Here</text>
      <g class="body-copy" font-size="6.4" fill="var(--white)"><text x="362" y="269">Lorem Ipsum is simply dummy</text><text x="362" y="280">text of the printing and type</text><text x="362" y="291">setting industry. Lorem Ipsum</text><text x="362" y="302">has been the industry's.</text></g>
    </g>
    <g class="service">
      <circle cx="538" cy="221" r="14" fill="var(--white)"/>
      <path d="M532 213h12v5a6 6 0 0 1-12 0z" fill="none" stroke="var(--navy)" stroke-width="1.3"/>
      <path d="M538 224v4M534 229h8" stroke="var(--navy)" stroke-width="1.3"/>
      <text class="headline" x="523" y="255" font-size="9.5" fill="var(--white)">Text In Here</text>
      <g class="body-copy" font-size="6.4" fill="var(--white)"><text x="523" y="269">Lorem Ipsum is simply dummy</text><text x="523" y="280">text of the printing and type</text><text x="523" y="291">setting industry. Lorem Ipsum</text><text x="523" y="302">has been the industry's.</text></g>
    </g>

    <circle cx="203" cy="367" r="2.5" fill="none" stroke="var(--white)"/>
    <line x1="206" y1="367" x2="255" y2="367" stroke="var(--white)"/>
    <text class="body-copy" x="342" y="370" text-anchor="middle" font-size="7" letter-spacing="1.6" fill="var(--white)">www.velorinathletic.example</text>
    <line x1="429" y1="367" x2="478" y2="367" stroke="var(--white)"/>
    <circle cx="481" cy="367" r="2.5" fill="none" stroke="var(--white)"/>
  </svg>
  <div class="slide-label slide-label--bottom slide-label--right">PAGE - 03</div>

</div>
</body>
</html>
```